Beer Can Labels Graphic Design

We need beer can label ideas for 4 different types of beer that we are producing. The 4 names and info required for each beer are as follows:

1. TMSPA. 6.0% ABV. 40 IBU. Strong Ale / Ale Forte. Indian Pale Ale

2. LunWitty Orange. 5.0% ABV. 10 IBU. Ale / Ale. Belgian Witbier. Brewed with Citrus peels and coriander

3. Marrow Pale Ale 5.2% ABV. 30 IBU. Ale / Biere. Honey Rye Ale

4. Wellsden Cove 3.2% ABV. 13 IBU. Light Ale / Ale Leger. Brown Ale

We would like to include our brewery name/logo "Tamsworth Brewing Company" on each of the can lables.

A bit of background:

TMSPA is an acronym of our company name with a bit of play on the local school "Tamsworth Gospel Academy" which most locals enjoy as their is some humor in a beer named after a bible school.

The last 3 names are after each of the communities that each of the 3 owners grew up at. Lunmore, Marrow Ridge and Wellsden.

Lunmore is recognized by a large grain elevator witin the area.

Marrow Rhidge is recognized by a creek and ball diamonds.

Wellsden is recognized by the castellane ferry, badlands/hoodos.

One thing each community has in common is the fact that all 3 are farming communities.

We are packaging utilizing standard 355ml cans so the graphic design must fit on a 7.375" x 3.125".

I will attach our logo as well as some of our current ideas/graphics for reference or use.
Updates

Project Deadline Extended Reason: Wanted to add a bit more time as there has been limited designs submitted as of right now. Added Friday, September 29, 2017

Target Market(s)

Beer Drinkers

Industry/Entity Type

Brewery

Requirements
Must have
• Beer names in color and required info (ie alcohol content and beer in english and french)
• Company name/logo
Nice to have
• A section which can be utilized to insert a brief story with each beer.
• Scale to define beer type on 3 items. Malt, hop and color
• Something consistent from beer to beer so that it can be easily modified for new beers we develop.
• Possibly a picture faded in the background or our company logo.
Should not have
• Too busy or too much going on.

```html
<!DOCTYPE html>
<html lang="en">
<head>
<meta charset="utf-8">
<title>Tamsworth Brewing Company – Can Labels</title>
<link rel="stylesheet" href="https://fonts.googleapis.com/css2?family=Oswald:wght@400;500;600&family=Yellowtail&family=Montserrat:wght@600;700;800&display=swap">
<style>
  :root{
    --orange:#f58220;
    --black:#0c0c0c;
    --green:#1fa64a;
    --grey:#a9a9a9;
    --grey-name:#b3b3b3;
    --white:#ffffff;
    --ink:#0c0c0c;
  }
  *{box-sizing:border-box;margin:0;padding:0}
  html,body{width:702px;height:1200px;overflow:hidden;background:var(--white)}
  .sheet{position:relative;width:702px;height:1200px}
  .band{position:absolute;left:0;width:702px;height:295px;background:var(--band)}
  .band--witbier{top:0;--band:var(--orange);--name:var(--orange);--panel-ink:var(--ink);--panel-line:var(--ink)}
  .band--brown{top:302px;--band:var(--black);--name:var(--ink);--panel-ink:var(--white);--panel-line:var(--white)}
  .band--ipa{top:603px;--band:var(--green);--name:var(--green);--panel-ink:var(--ink);--panel-line:var(--ink)}
  .band--pale{top:905px;--band:var(--grey);--name:var(--grey-name);--panel-ink:var(--ink);--panel-line:var(--ink)}

  /* front label */
  .front{position:absolute;left:50px;top:12px;width:253px;height:271px;background:var(--white);
    border:2px solid var(--ink);border-radius:9px;overflow:hidden}
  .front__brand{position:absolute;left:9px;right:9px;top:7px;height:24px;border:2px solid var(--ink);
    border-radius:3px;font:500 15px/20px "Oswald",sans-serif;text-align:center;color:var(--ink);letter-spacing:-.2px;white-space:nowrap}
  .front__name{position:absolute;left:10px;right:10px;top:36px;font:400 46px/44px "Yellowtail",cursive;
    color:var(--name);text-align:center;white-space:nowrap}
  .front__name--one{font-size:54px;top:46px}
  .front__art{position:absolute;background:var(--ink)}
  .front__panel{position:absolute;left:0;right:0;top:176px;height:62px;background:var(--ink);color:var(--white);padding:4px 12px 0}
  .front__style{font:700 19px/23px "Montserrat",sans-serif;letter-spacing:1px;text-align:center;white-space:nowrap}
  .front__style--wide{letter-spacing:4px;font-size:25px;line-height:26px}
  .front__note{font:400 11px/13px "Oswald",sans-serif;color:var(--orange);text-align:center;white-space:nowrap}
  .front__stats{display:flex;justify-content:space-between;font:700 14px/18px "Montserrat",sans-serif;padding:0 2px;white-space:nowrap}
  .front__class{position:absolute;left:7px;right:7px;bottom:6px;height:24px;border:2px solid var(--ink);
    border-radius:4px;font:700 14px/20px "Montserrat",sans-serif;text-align:center;color:var(--ink);letter-spacing:.3px;background:var(--white);white-space:nowrap}

  /* side ingredients */
  .ingredients{position:absolute;left:372px;top:12px;height:271px;width:34px;writing-mode:vertical-rl;transform:rotate(180deg);
    font:italic 400 4.4px/5.5px "Oswald",sans-serif;color:var(--panel-ink);text-align:justify}
  .band--witbier .ingredients,.band--ipa .ingredients,.band--pale .ingredients{color:var(--ink)}
  .ingredients b{font-weight:600}

  /* back panel */
  .back{position:absolute;left:416px;top:11px;width:254px;height:274px;border:2px solid var(--panel-line);border-radius:7px;overflow:hidden;color:var(--panel-ink)}
  .back__brand{margin:5px;height:100px;border:3px solid var(--panel-line);border-radius:6px;text-align:center;padding-top:4px;white-space:nowrap}
  .back__brand-name{display:block;font:600 42px/56px "Oswald",sans-serif;letter-spacing:0}
  .back__brand-sub{display:block;font:500 24px/30px "Oswald",sans-serif;letter-spacing:.3px}
  .back__story{margin:6px 12px 0;font:400 6.3px/8px "Oswald",sans-serif;text-transform:uppercase;text-align:justify;letter-spacing:.15px}
  .back__art{position:absolute;background:var(--panel-ink)}
</style>
</head>
<body>
<main class="sheet">

  <section class="band band--witbier">
    <article class="front">
      <div class="front__brand">TAMSWORTH BREWING COMPANY</div>
      <h2 class="front__name">LunWitty<br>Orange</h2>
      <div class="front__art" role="img" aria-label="Grain elevator silhouette" style="right:0;top:132px;width:46px;height:56px"></div>
      <div class="front__panel">
        <p class="front__style">BELGIAN WITBIER</p>
        <p class="front__note">Brewed with Citrus Peels &amp; Coriander</p>
        <p class="front__stats"><span>5.0% alc./vol.</span><span>10 IBU</span></p>
      </div>
      <div class="front__class">ALE/ALE</div>
    </article>
    <p class="ingredients"><b>INGREDIENTS:</b> water, malted barley, malted wheat, oats, hops, yeast. Brewed and canned in small batches by hand. Keep cold and enjoy fresh. Please drink responsibly.</p>
    <article class="back">
      <header class="back__brand"><span class="back__brand-name">TAMSWORTH</span><span class="back__brand-sub">BREWING COMPANY</span></header>
      <p class="back__story">Lorem ipsum dolor sit amet, consectetur adipiscing elit, sed do eiusmod tempor incididunt ut labore et dolore magna aliqua. Ut enim ad minim veniam, quis nostrud exercitation ullamco laboris nisi ut aliquip ex ea commodo consequat. Duis aute irure dolor in reprehenderit in voluptate velit esse cillum dolore eu fugiat nulla pariatur. Excepteur sint occaecat cupidatat non proident, sunt in culpa qui officia deserunt mollit anim id est laborum. Sed ut perspiciatis unde omnis iste natus error sit voluptatem accusantium doloremque laudantium, totam rem aperiam, eaque ipsa quae ab illo inventore veritatis et quasi architecto beatae vitae dicta sunt explicabo. Nemo enim ipsam voluptatem quia voluptas sit aspernatur aut odit aut.</p>
      <div class="back__art" role="img" aria-label="Prairie and grain elevator silhouette" style="left:0;right:0;bottom:0;height:36px"></div>
    </article>
  </section>

  <section class="band band--brown">
    <article class="front">
      <div class="front__brand">TAMSWORTH BREWING COMPANY</div>
      <h2 class="front__name">Wellsden<br>Cove</h2>
      <div class="front__art" role="img" aria-label="Badlands and hoodoo silhouette" style="left:0;right:0;top:140px;height:40px"></div>
      <div class="front__panel">
        <p class="front__style front__style--wide" style="margin-top:6px">BROWN ALE</p>
        <p class="front__stats" style="margin-top:4px"><span>3.2% alc./vol.</span><span>13 IBU</span></p>
      </div>
      <div class="front__class">LIGHT ALE/ALE LÉGÉRÉ</div>
    </article>
    <p class="ingredients"><b>INGREDIENTS:</b> water, malted barley, malted wheat, oats, hops, yeast. Brewed and canned in small batches by hand. Keep cold and enjoy fresh. Please drink responsibly.</p>
    <article class="back">
      <header class="back__brand"><span class="back__brand-name">TAMSWORTH</span><span class="back__brand-sub">BREWING COMPANY</span></header>
      <p class="back__story">Lorem ipsum dolor sit amet, consectetur adipiscing elit, sed do eiusmod tempor incididunt ut labore et dolore magna aliqua. Ut enim ad minim veniam, quis nostrud exercitation ullamco laboris nisi ut aliquip ex ea commodo consequat. Duis aute irure dolor in reprehenderit in voluptate velit esse cillum dolore eu fugiat nulla pariatur. Excepteur sint occaecat cupidatat non proident, sunt in culpa qui officia deserunt mollit anim id est laborum. Sed ut perspiciatis unde omnis iste natus error sit voluptatem accusantium doloremque laudantium, totam rem aperiam, eaque ipsa quae ab illo inventore veritatis et quasi architecto beatae vitae dicta sunt explicabo.</p>
      <div class="back__art" role="img" aria-label="Badlands and hoodoo silhouette" style="left:10px;right:10px;bottom:12px;height:56px"></div>
    </article>
  </section>

  <section class="band band--ipa">
    <article class="front">
      <div class="front__brand">TAMSWORTH BREWING COMPANY</div>
      <h2 class="front__name front__name--one">TMSPA</h2>
      <div class="front__art" role="img" aria-label="School building silhouette" style="left:36px;right:24px;top:110px;height:68px"></div>
      <div class="front__panel">
        <p class="front__style" style="margin-top:6px">INDIAN PALE ALE</p>
        <p class="front__stats" style="margin-top:4px"><span>6.0% alc./vol.</span><span>40 IBU</span></p>
      </div>
      <div class="front__class">STRONG ALE/ALE FORTÉ</div>
    </article>
    <p class="ingredients"><b>INGREDIENTS:</b> water, malted barley, malted wheat, oats, hops, yeast. Brewed and canned in small batches by hand. Keep cold and enjoy fresh. Please drink responsibly.</p>
    <article class="back">
      <header class="back__brand"><span class="back__brand-name">TAMSWORTH</span><span class="back__brand-sub">BREWING COMPANY</span></header>
      <p class="back__story">Lorem ipsum dolor sit amet, consectetur adipiscing elit, sed do eiusmod tempor incididunt ut labore et dolore magna aliqua. Ut enim ad minim veniam, quis nostrud exercitation ullamco laboris nisi ut aliquip ex ea commodo consequat. Duis aute irure dolor in reprehenderit in voluptate velit esse cillum dolore eu fugiat nulla pariatur. Excepteur sint occaecat cupidatat non proident, sunt in culpa qui officia deserunt mollit anim id est laborum. Sed ut perspiciatis unde omnis iste natus error sit voluptatem accusantium doloremque laudantium, totam rem aperiam, eaque ipsa quae ab illo inventore veritatis et quasi architecto beatae vitae dicta sunt explicabo. Nemo enim ipsam voluptatem quia voluptas sit aspernatur aut odit aut fugit, sed quia consequuntur magni dolores eos qui ratione voluptatem sequi nesciunt.</p>
      <div class="back__art" role="img" aria-label="School building silhouette" style="left:132px;right:8px;bottom:8px;height:40px"></div>
    </article>
  </section>

  <section class="band band--pale">
    <article class="front">
      <div class="front__brand">TAMSWORTH BREWING COMPANY</div>
      <h2 class="front__name">Marrow<br>Pale Ale</h2>
      <div class="front__art" role="img" aria-label="Pitcher silhouette" style="left:26px;width:38px;top:122px;height:48px"></div>
      <div class="front__art" role="img" aria-label="Batter silhouette" style="right:18px;width:30px;top:118px;height:52px"></div>
      <div class="front__panel">
        <p class="front__style front__style--wide" style="font-size:30px;line-height:30px;margin-top:2px">PALE ALE</p>
        <p class="front__stats"><span>5.2% alc./vol.</span><span>30 IBU</span></p>
      </div>
      <div class="front__class">ALE/ALE</div>
    </article>
    <p class="ingredients"><b>INGREDIENTS:</b> water, malted barley, malted wheat, oats, hops, yeast. Brewed and canned in small batches by hand. Keep cold and enjoy fresh. Please drink responsibly.</p>
    <article class="back">
      <header class="back__brand"><span class="back__brand-name">TAMSWORTH</span><span class="back__brand-sub">BREWING COMPANY</span></header>
      <p class="back__story">Lorem ipsum dolor sit amet, consectetur adipiscing elit, sed do eiusmod tempor incididunt ut labore et dolore magna aliqua. Ut enim ad minim veniam, quis nostrud exercitation ullamco laboris nisi ut aliquip ex ea commodo consequat. Duis aute irure dolor in reprehenderit in voluptate velit esse cillum dolore eu fugiat nulla pariatur. Excepteur sint occaecat cupidatat non proident, sunt in culpa qui officia deserunt mollit anim id est laborum. Sed ut perspiciatis unde omnis iste natus error sit voluptatem accusantium doloremque laudantium, totam rem aperiam, eaque ipsa quae ab illo inventore veritatis et quasi architecto beatae vitae dicta sunt explicabo. Nemo enim ipsam voluptatem quia voluptas sit aspernatur aut odit aut fugit, sed quia consequuntur magni dolores eos qui ratione voluptatem sequi nesciunt.</p>
      <div class="back__art" role="img" aria-label="Pitcher silhouette" style="left:22px;width:34px;bottom:10px;height:36px"></div>
      <div class="back__art" role="img" aria-label="Batter silhouette" style="right:20px;width:26px;bottom:12px;height:40px"></div>
    </article>
  </section>

</main>
</body>
</html>
```